Business Card Design Project

Business Card
We are rebranding with a new logo
Industry/Entity Type
Business
Contact Information for Business Card
Dennis Marlow +61 427581962 dennis@qovo.com.au P.O. Box 872 Kelvindale QLD 4309
Requirements
Must have
- Logo

```html
<!DOCTYPE html>
<html lang="en">
<head>
<meta charset="utf-8">
<title>Qovo International – Business Card</title>
<link href="https://fonts.googleapis.com/css2?family=Mulish:wght@700&display=swap" rel="stylesheet">
<style>
  :root {
    --page-bg: #e8e8e8;
    --card-white: #ffffff;
    --pattern-light: #f6fafd;
    --pattern-tint: #eaf3fa;
    --band-blue: #2a7fd8;
    --deep-blue: #1a5cb0;
    --panel-blue: #1ea6ec;
    --brand-navy: #1d4f91;
    --text-light: #ffffff;
  }
  * { margin: 0; padding: 0; box-sizing: border-box; }
  html, body {
    width: 1200px;
    height: 901px;
    overflow: hidden;
    background: var(--page-bg);
    font-family: "Mulish", "Century Gothic", sans-serif;
  }
  .business-card {
    position: absolute;
    left: 100px;
    top: 148px;
    width: 1000px;
    height: 606px;
    background: var(--card-white);
    box-shadow: 0 10px 30px rgba(0,0,0,0.18);
    overflow: hidden;
  }
  .pattern-field {
    position: absolute;
    left: 0;
    top: 0;
    width: 470px;
    height: 606px;
    background: linear-gradient(135deg, var(--pattern-light), var(--pattern-tint));
  }
  .graphic-field {
    position: absolute;
    left: 470px;
    top: 0;
    width: 530px;
    height: 606px;
    background: linear-gradient(90deg, var(--band-blue) 0%, var(--deep-blue) 22%, var(--panel-blue) 45%, var(--panel-blue) 100%);
  }
  .brand-name {
    position: absolute;
    left: 55px;
    top: 225px;
    color: var(--brand-navy);
    font-weight: 700;
    line-height: 1;
  }
  .brand-main {
    display: block;
    font-size: 112px;
    letter-spacing: -1px;
  }
  .brand-sub {
    display: block;
    font-size: 33px;
    letter-spacing: 4px;
    margin-top: 14px;
    margin-left: 4px;
  }
  .contact-block {
    position: absolute;
    color: var(--text-light);
    font-weight: 700;
    white-space: nowrap;
  }
  .person-name {
    left: 612px;
    top: 128px;
    font-size: 46px;
    letter-spacing: 0.5px;
  }
  .contact-line {
    display: flex;
    align-items: center;
    gap: 12px;
  }
  .contact-phone {
    left: 576px;
    top: 246px;
    font-size: 38px;
    letter-spacing: 1px;
  }
  .contact-email {
    left: 543px;
    top: 316px;
    font-size: 35px;
    letter-spacing: 0.5px;
  }
  .contact-address {
    left: 568px;
    top: 376px;
    font-size: 30px;
    align-items: flex-start;
    gap: 10px;
  }
  .address-text {
    line-height: 1.3;
    text-align: center;
  }
  .contact-icon { flex: none; }
</style>
</head>
<body>
  <div class="business-card">
    <div class="pattern-field" role="img" aria-label="Faint light-blue line pattern background"></div>
    <div class="graphic-field" role="img" aria-label="Layered blue geometric graphic behind the contact details"></div>

    <div class="brand-name">
      <span class="brand-main">Qovo</span>
      <span class="brand-sub">INTERNATIONAL</span>
    </div>

    <div class="contact-block person-name">Dennis Marlow</div>

    <div class="contact-block contact-line contact-phone">
      <svg class="contact-icon" width="32" height="32" viewBox="0 0 24 24" aria-hidden="true">
        <path fill="#fff" d="M6.6 10.8a15.2 15.2 0 0 0 6.6 6.6l2.2-2.2c.3-.3.7-.4 1-.2 1.1.4 2.3.6 3.6.6.6 0 1 .4 1 1V20c0 .6-.4 1-1 1A17 17 0 0 1 3 4c0-.6.4-1 1-1h3.5c.6 0 1 .4 1 1 0 1.3.2 2.5.6 3.6.1.3 0 .7-.2 1z"/>
      </svg>
      <span>+61 427581962</span>
    </div>

    <div class="contact-block contact-line contact-email">
      <svg class="contact-icon" width="36" height="26" viewBox="0 0 36 26" aria-hidden="true">
        <rect x="1" y="2" width="34" height="22" fill="#fff"/>
        <polyline points="1,2 18,15 35,2" fill="none" stroke="var(--panel-blue)" stroke-width="2.5"/>
      </svg>
      <span>dennis@qovo.com.au</span>
    </div>

    <div class="contact-block contact-line contact-address">
      <svg class="contact-icon" width="54" height="30" viewBox="0 0 54 30" aria-hidden="true">
        <line x1="0" y1="8" x2="14" y2="8" stroke="#fff" stroke-width="2.5"/>
        <line x1="4" y1="15" x2="16" y2="15" stroke="#fff" stroke-width="2.5"/>
        <line x1="8" y1="22" x2="18" y2="22" stroke="#fff" stroke-width="2.5"/>
        <rect x="20" y="5" width="32" height="21" fill="#fff"/>
        <polyline points="20,5 36,17 52,5" fill="none" stroke="var(--panel-blue)" stroke-width="2.5"/>
      </svg>
      <span class="address-text">P.O. Box 872<br>Kelvindale QLD 4309</span>
    </div>
  </div>
</body>
</html>
```